My name is Delia Forsythe,I want to create a web page for my personal dog grooming business. The name on the web page can be "Delia's Dog Grooming" I am located in San Antonio Texas. The page would help grow my customer base. Before and after pictures would display the quality of work that I do. On my page I can provide information about myself, my services, and pricing.
Updates

I have updated project to guaranteed pay

Please try to incorporate a schnauzer in an icon or logo. My dog is a schnauzer. THANKS!!!!!!!!!!!!

Target Market(s)

Dog Owners

Industry/Entity Type

Business

Requirements
Must have
• -A spot for before and after pictures.
-An about me section
-A section to make an appointment
Nice to have
• My favorite Color is purple. I think different shades of purple would be nice or purple with a light green

please incorporate a schnauzer in any icon or logo. My dog is a schnauzer.

```html
<!DOCTYPE html>
<html lang="en">
<head>
<meta charset="utf-8">
<title>Delia's Dog Grooming</title>
<link rel="stylesheet" href="https://fonts.googleapis.com/css2?family=Tinos:ital,wght@0,400;0,700;1,400&family=PT+Sans:ital,wght@0,400;1,400&display=swap">
<style>
:root{
  --cream:#f9f7ee;
  --blush:#fdeef3;
  --hero:#fce8f0;
  --plum:#9b3f6e;
  --plum-soft:#a04d7b;
  --plum-dark:#70304f;
  --ink:#2b1222;
  --button:#f6dce7;
  --sage:#e9ecdc;
  --sage-line:#dfe5cf;
  --frame:#fbfaf3;
  --photo-a:#8d2f5e;
  --photo-b:#c37a9c;
}
*{margin:0;padding:0;box-sizing:border-box}
html,body{width:1200px;height:850px;overflow:hidden}
body{position:relative;background:var(--cream);font-family:"PT Sans",Arial,sans-serif;color:var(--ink)}
.abs{position:absolute}
.serif{font-family:"Tinos","Times New Roman",serif}
.line{display:block;white-space:nowrap}

.nav-strip{left:0;top:118px;width:1200px;height:45px;background:var(--blush);border-top:1px solid #f6e0e8;border-bottom:1px solid #f6e0e8}
.hero{left:0;top:163px;width:1200px;height:357px;background:var(--hero)}
.hero-edge{left:0;top:512px;width:1200px;height:12px}

.brand{left:84px;top:30px;width:420px;height:205px}
.brand-dot{left:160px;top:102px;width:40px;height:40px;border-radius:50%;background:#fff}
.brand-name{left:205px;top:92px;width:250px;text-align:center;color:#fff;font-size:31px;line-height:1.1;letter-spacing:1px}

.gallery-photo{left:736px;top:16px;width:108px;height:92px;background:#fff;transform:rotate(-8deg);box-shadow:0 2px 4px rgba(0,0,0,.25);padding:7px}
.gallery-photo-back{left:752px;top:14px;width:104px;height:94px;background:#fff;transform:rotate(4deg);box-shadow:0 2px 4px rgba(0,0,0,.2)}
.gallery-photo .shot{width:100%;height:100%;background:linear-gradient(135deg,#d9d6cf,#8e8a84)}
.gallery-link{left:873px;top:38px;color:var(--plum);font-size:21px;line-height:24px;letter-spacing:2.2px;text-transform:uppercase}

.main-nav{left:577px;top:131px;display:flex;list-style:none;font-weight:700;font-size:15px;letter-spacing:2.4px;color:var(--plum-dark)}
.main-nav li{margin-right:33px}
.main-nav li:last-child{margin-right:0}

.welcome{left:81px;top:254px;width:480px;font-size:30px;line-height:34px;color:var(--plum-soft);font-weight:400;letter-spacing:-.5px}
.intro{left:81px;top:338px;font-size:14.5px;line-height:19.5px;color:var(--ink);letter-spacing:-.3px}
.services-btn{left:95px;top:435px;width:415px;height:55px;background:var(--button);border-radius:3px;display:flex;align-items:center;justify-content:center;gap:10px;color:var(--plum-soft);font-size:22px;letter-spacing:-.3px;text-shadow:0 1px 0 #fff}
.services-btn .dot{width:22px;height:22px;border-radius:50%;background:var(--plum-soft)}

.frame-back{background:var(--frame);box-shadow:0 1px 4px rgba(0,0,0,.2)}
.frame-back .shot{position:absolute;inset:6px;background:linear-gradient(120deg,#6f7d3f,#a7b56a)}
.frame-main{left:575px;top:203px;width:505px;height:263px;background:var(--frame);box-shadow:0 2px 6px rgba(0,0,0,.25);padding:6px}
.frame-main .shot{width:100%;height:100%;background:linear-gradient(100deg,var(--photo-a) 0%,var(--photo-b) 55%,var(--photo-a) 100%)}
.slider-dots{left:784px;top:489px;display:flex;gap:4px}
.slider-dots span{width:14px;height:14px;border-radius:50%;background:#f7f3f0;border:1px solid #ddd3d6;position:relative}
.slider-dots span.on::after{content:"";position:absolute;left:4px;top:4px;width:4px;height:4px;border-radius:50%;background:var(--plum)}

.phone-art{left:95px;top:550px;width:128px;height:90px;border-radius:10px;background:linear-gradient(180deg,#c98aab,#a2507d)}
.inquiries-title{left:250px;top:539px;font-size:28px;letter-spacing:6px;color:var(--plum-soft)}
.inquiries-rule{left:326px;top:581px;width:110px;height:0;border-top:2px solid var(--plum-soft)}
.inquiries-phone{left:247px;top:589px;font-size:35px;letter-spacing:7px;color:var(--plum-soft)}
.inquiries-web{left:247px;top:629px;font-size:14.5px;letter-spacing:3.2px;color:var(--plum-soft)}

.reviews-title{left:576px;top:538px;font-size:19px;font-weight:400;color:var(--plum);letter-spacing:-.2px}
.review{left:578px;top:568px;font-size:15px;line-height:19px;color:var(--plum);letter-spacing:-.2px}
.reviewer{left:579px;top:632px;font-size:15px;font-style:italic;color:var(--plum);letter-spacing:-.4px}

.dotted-rule{left:0;top:673px;width:1200px;height:0;border-top:4px dotted #e2e6d7}
.sage-band{left:6px;top:681px;width:1194px;height:17px;background:var(--sage-line)}
.footer-bar{left:0;top:707px;width:1200px;height:48px;background:var(--cream);border-top:2px solid #f0efe9;border-bottom:2px solid #e4e3dc}
.footer-nav{left:88px;top:723px;display:flex;list-style:none;font-weight:700;font-size:11px;letter-spacing:2.2px;color:var(--plum-dark)}
.footer-nav li{margin-right:24px}
.social{top:721px;display:flex;align-items:center;gap:10px;font-size:12px;color:var(--plum-dark);text-transform:uppercase}
.social b{font-weight:400;font-size:13px;color:var(--plum);text-transform:none}
.follow{left:823px}
.find{left:973px}
.footer{left:0;top:758px;width:1200px;height:87px;background:var(--sage)}
.copyright{left:0;top:786px;width:1200px;display:flex;justify-content:center;align-items:center;gap:8px;font-size:15px;letter-spacing:3px;color:var(--plum-soft)}
.copyright .dot{width:20px;height:20px;border-radius:50%;background:var(--plum-soft)}
</style>
</head>
<body>

<div class="abs nav-strip"></div>
<div class="abs hero"></div>
<svg class="abs hero-edge" viewBox="0 0 1200 12" preserveAspectRatio="none" aria-hidden="true">
  <defs>
    <pattern id="scallop" width="10" height="12" patternUnits="userSpaceOnUse"><path d="M0 12 L0 8 Q5 2 10 8 L10 12 Z" fill="var(--cream)"/></pattern>
  </defs>
  <rect width="1200" height="12" fill="url(#scallop)"/>
</svg>

<header>
  <svg class="abs brand" viewBox="0 0 420 205" aria-hidden="true">
    <path d="M40 12 Q60 2 120 6 L395 6 Q418 8 416 35 L408 130 Q405 158 378 160 L230 168 L205 200 L198 168 L60 160 Q30 156 22 128 L5 60 Q0 22 40 12 Z" fill="#f7e9f0" stroke="#fff" stroke-width="4"/>
    <path d="M52 40 Q58 26 90 26 L380 28 Q398 30 394 50 L386 120 Q383 140 360 142 L80 138 Q62 136 58 118 L42 62 Q40 48 52 40 Z" fill="var(--plum)"/>
  </svg>
  <span class="abs brand-dot"></span>
  <div class="abs brand-name serif">Delia's Dog Grooming</div>

  <div class="abs gallery-photo-back"></div>
  <div class="abs gallery-photo"><div class="shot" role="img" aria-label="Photo of a groomed schnauzer in a red bandana"></div></div>
  <a class="abs gallery-link serif">Check out our<br>photo gallery</a>

  <ul class="abs main-nav serif">
    <li>INFORMATION</li><li>SERVICES</li><li>PRICING</li><li>CONTACT</li>
  </ul>
</header>

<main>
  <h1 class="abs welcome serif">Welcome to Delia’s Dog Grooming.<br>We are located in San Antonio Texas</h1>
  <p class="abs intro">
    <span class="line">Lorem ipsum dolor sit amet, consectetur adipisicing elit, sed do eiusmod</span>
    <span class="line">tempor incididunt ut labore et dolore magna aliqua. Ut enim ad minim</span>
    <span class="line">veniam, quis nostrud exercitation ullamco laboris nisi ut aliquip ex ea com-</span>
    <span class="line">modo consequat. Duis aute irure dolor in reprehenderit in voluptate velit</span>
  </p>
  <a class="abs services-btn serif"><span class="dot"></span>CHECK OUT OUR SERVICES</a>

  <div class="abs frame-back" style="left:592px;top:175px;width:480px;height:300px;transform:rotate(-2deg)"><div class="shot"></div></div>
  <div class="abs frame-back" style="left:568px;top:215px;width:525px;height:265px;transform:rotate(1.5deg)"><div class="shot"></div></div>
  <div class="abs frame-main"><div class="shot" role="img" aria-label="Groomer blow-drying a long-haired dog in a plum salon"></div></div>
  <div class="abs slider-dots"><span></span><span class="on"></span><span></span><span></span><span></span></div>

  <section>
    <div class="abs phone-art" role="img" aria-label="Illustration of a vintage rotary telephone"></div>
    <div class="abs inquiries-title serif">ALL INQUIRIES</div>
    <div class="abs inquiries-rule"></div>
    <div class="abs inquiries-phone serif">555.418.7720</div>
    <div class="abs inquiries-web serif">DELIASDOGGROOMING.COM</div>
  </section>

  <section>
    <h2 class="abs reviews-title serif">What Our Customers Are Saying</h2>
    <p class="abs review">
      <span class="line">This was my puppy's first grooming experience so we were both pretty ner-</span>
      <span class="line">vous! It was great! My puppy was very calm and looked wonderful! I will never</span>
      <span class="line">go anywhere else!</span>
    </p>
    <p class="abs reviewer">Customers Name, Satisfied Customer</p>
  </section>
</main>

<div class="abs dotted-rule"></div>
<div class="abs sage-band"></div>

<footer>
  <div class="abs footer-bar"></div>
  <ul class="abs footer-nav serif">
    <li>INFORMATION</li><li>SERVICES</li><li>PRICING</li><li>CONTACT</li>
  </ul>
  <div class="abs social follow">Follow us on <b>Chirper</b></div>
  <div class="abs social find">Find us on <b>Facespace</b></div>
  <div class="abs footer"></div>
  <div class="abs copyright serif"><span class="dot"></span>©DELIASDOGGROOMING</div>
</footer>

</body>
</html>
```